Amber Lantern Studio - Needs image for website and marketing materials

Amber Lantern Studio needs a graphic design to visually communicate their cloud based fertility organizer app. We would like to see bright colors used that work well with the pink in our logo. The design should communicate that a complex process is easier to manage with our app.

You can get more details about our app at www.amberlanternstudio-app.example

Target Market(s)

Women that are pursuing a family (20 something - 40 something)

Industry/Entity Type

Graphic Design

Requirements
Must have
• The design should include an Korvix image to communicate our app can be used by smartphones. This image may be used on website, posters and other marketing materials.
I have added 3 files to the project. Use the general png image for the Korvix app screen and not the one with the phone image with the screen shot.
Nice to have
• I would like to connect the colors already used for each of the categories within the app to maybe icons that represent these categories (appointment, medication, lab test, procedures, natural) like is displayed in the sample images attached.

```html
<!DOCTYPE html>
<html lang="en">
<head>
<meta charset="utf-8">
<title>Amber Lantern Studio – Korvix App Hero</title>
<link href="https://fonts.googleapis.com/css2?family=Arimo:wght@400;700&display=swap" rel="stylesheet">
<style>
  :root{
    --bg:#ffffff;
    --device:#141414;
    --device-edge:#3a3a3a;
    --screen:#f2f2f2;
    --status:#1a1a1a;
    --chrome:#d9dde3;
    --pink:#ec3f7c;
    --appointment:#b9a3d6;
    --medication:#f4f07a;
    --labtest:#e88a92;
    --procedure:#8fd0df;
    --natural:#c9e29a;
    --label:#9a9a9a;
    --ink:#222222;
  }
  *{box-sizing:border-box;margin:0;padding:0}
  html,body{width:1200px;height:638px;overflow:hidden;background:var(--bg)}
  body{font-family:"Arimo",Arial,sans-serif;position:relative}

  .app-tile{position:absolute;border-radius:18%;
    box-shadow:0 4px 10px rgba(0,0,0,.25), inset 0 0 0 2px rgba(255,255,255,.35)}
  .app-tile::after{content:"";position:absolute;inset:0;border-radius:inherit;
    background:linear-gradient(160deg,rgba(255,255,255,.45) 0%,rgba(255,255,255,0) 45%)}

  .device{position:absolute;left:450px;top:-6px;width:292px;height:636px;
    background:var(--device);border-radius:46px;border:3px solid var(--device-edge);
    box-shadow:0 6px 18px rgba(0,0,0,.35)}
  .device-speaker{position:absolute;left:118px;top:22px;width:56px;height:7px;border-radius:4px;background:#333}
  .device-camera{position:absolute;left:140px;top:6px;width:9px;height:9px;border-radius:50%;background:#2a2a2a}
  .device-home{position:absolute;left:116px;top:554px;width:56px;height:56px;border-radius:50%;
    border:3px solid #333;background:#0c0c0c}
  .device-home::after{content:"";position:absolute;left:16px;top:16px;width:18px;height:18px;
    border:2px solid #555;border-radius:4px}

  .screen{position:absolute;left:18px;top:100px;width:250px;height:428px;background:var(--screen);
    overflow:hidden;font-size:11px;color:var(--ink)}
  .status-bar{height:16px;background:var(--status);color:#fff;font-size:9px;
    display:flex;justify-content:space-between;align-items:center;padding:0 6px}
  .browser-bar{background:var(--chrome);padding:3px 6px 6px;border-bottom:1px solid #b8bec7}
  .browser-title{text-align:center;font-size:10px;color:#444;margin-bottom:3px}
  .browser-fields{display:flex;gap:5px}
  .url-field,.search-field{background:#fff;border:1px solid #aab;border-radius:10px;height:18px;
    font-size:9px;line-height:16px;padding:0 7px;color:#555;white-space:nowrap;overflow:hidden}
  .url-field{flex:1}
  .search-field{width:70px;color:#aaa}

  .page-header{background:var(--pink);color:#fff;height:30px;position:relative;
    display:flex;align-items:center;justify-content:center;font-weight:700;font-size:14px}
  .back-button{position:absolute;left:6px;top:7px;background:#fff;color:var(--pink);
    font-size:8px;font-weight:700;border-radius:3px;padding:2px 6px}
  .event-list{padding:6px 6px 0}
  .event-label{color:var(--label);font-weight:700;font-size:10px;padding:4px 4px 5px}
  .event-row{height:36px;border-radius:6px;margin-bottom:5px;font-weight:700;font-size:11px;
    display:flex;align-items:center;padding-left:8px}
  .row-appointment{background:var(--appointment)}
  .row-medication{background:var(--medication)}
  .row-labtest{background:var(--labtest)}
  .row-procedure{background:var(--procedure)}
  .row-natural{background:var(--natural)}
  .browser-toolbar{position:absolute;left:0;bottom:0;width:100%;height:32px;
    background:linear-gradient(#c4cad3,#a6aeb9);display:flex;justify-content:space-around;align-items:center}
  .browser-toolbar svg{width:14px;height:14px;fill:#555}
</style>
</head>
<body>

<!-- small scattered tiles behind -->
<div class="app-tile" style="left:92px;top:224px;width:50px;height:50px;background:#b04ad0;transform:rotate(-14deg)" role="img" aria-label="Small purple app icon"></div>
<div class="app-tile" style="left:55px;top:272px;width:42px;height:42px;background:#3f7bd9;transform:rotate(8deg)" role="img" aria-label="Small blue app icon"></div>
<div class="app-tile" style="left:16px;top:238px;width:34px;height:34px;background:#f6a030;transform:rotate(-10deg)" role="img" aria-label="Small orange folder icon"></div>
<div class="app-tile" style="left:150px;top:240px;width:66px;height:66px;background:#4d7fe6;transform:rotate(-6deg)" role="img" aria-label="Heart monitor app icon"></div>
<div class="app-tile" style="left:66px;top:270px;width:70px;height:64px;background:#c654d8;transform:rotate(12deg)" role="img" aria-label="Thermometer app icon"></div>
<div class="app-tile" style="left:225px;top:210px;width:24px;height:24px;background:#f25a8a;transform:rotate(20deg)"></div>
<div class="app-tile" style="left:392px;top:150px;width:26px;height:26px;background:#37b7e8;transform:rotate(-18deg)"></div>
<div class="app-tile" style="left:408px;top:195px;width:18px;height:18px;background:#f04ad0;transform:rotate(12deg)"></div>
<div class="app-tile" style="left:372px;top:230px;width:20px;height:20px;background:#9acd32;transform:rotate(-8deg)"></div>
<div class="app-tile" style="left:760px;top:160px;width:22px;height:22px;background:#ff6a3a;transform:rotate(14deg)"></div>
<div class="app-tile" style="left:790px;top:200px;width:18px;height:18px;background:#3fb6e8;transform:rotate(-10deg)"></div>
<div class="app-tile" style="left:1116px;top:226px;width:64px;height:64px;background:#6ac23a;transform:rotate(18deg)" role="img" aria-label="Pencil app icon"></div>
<div class="app-tile" style="left:1006px;top:318px;width:60px;height:60px;background:#f05a90;transform:rotate(-12deg)" role="img" aria-label="Shopping cart app icon"></div>
<div class="app-tile" style="left:1020px;top:268px;width:74px;height:74px;background:#2fa84a;transform:rotate(8deg)" role="img" aria-label="Document app icon"></div>
<div class="app-tile" style="left:1090px;top:200px;width:30px;height:30px;background:#e83a3a;transform:rotate(-6deg)"></div>
<div class="app-tile" style="left:1150px;top:330px;width:26px;height:26px;background:#3a8fe0;transform:rotate(10deg)"></div>
<div class="app-tile" style="left:918px;top:226px;width:92px;height:86px;background:#4aa8e4;transform:rotate(14deg)" role="img" aria-label="Notepad app icon"></div>
<div class="app-tile" style="left:860px;top:282px;width:94px;height:88px;background:#9b4ad0;transform:rotate(-8deg)" role="img" aria-label="Calendar app icon"></div>

<!-- device -->
<div class="device">
  <div class="device-camera"></div>
  <div class="device-speaker"></div>
  <div class="screen">
    <div class="status-bar"><span>NetLink</span><span>1:36 PM</span><span>83%</span></div>
    <div class="browser-bar">
      <div class="browser-title">ALS Mobile</div>
      <div class="browser-fields">
        <div class="url-field">calendar.amberlanternstudio-app.example</div>
        <div class="search-field">Search</div>
      </div>
    </div>
    <div class="page-header"><span class="back-button">back</span>Add Event</div>
    <div class="event-list">
      <div class="event-label">Event Type</div>
      <div class="event-row row-appointment">Appointment</div>
      <div class="event-row row-medication">Medication</div>
      <div class="event-row row-labtest">Lab Test</div>
      <div class="event-row row-procedure">Procedure</div>
      <div class="event-row row-natural">Natural</div>
    </div>
    <div class="browser-toolbar">
      <svg viewBox="0 0 10 10"><path d="M7 1 2 5l5 4z"/></svg>
      <svg viewBox="0 0 10 10"><path d="M3 1l5 4-5 4z"/></svg>
      <svg viewBox="0 0 10 10"><path d="M1 4h5V1l4 4-4 4V6H1z"/></svg>
      <svg viewBox="0 0 10 10"><path d="M1 2h8v6H1z"/></svg>
      <svg viewBox="0 0 10 10"><path d="M1 3h6v6H1zM3 1h6v6H8V2H3z"/></svg>
    </div>
  </div>
  <div class="device-home"></div>
</div>

<!-- foreground tiles -->
<div class="app-tile" style="left:232px;top:226px;width:160px;height:160px;background:#4fc0ee;transform:rotate(-12deg)" role="img" aria-label="Clipboard app icon for appointments"></div>
<div class="app-tile" style="left:64px;top:350px;width:134px;height:134px;background:#2f9fb0;transform:rotate(-8deg)" role="img" aria-label="Magnifier app icon for lab tests"></div>
<div class="app-tile" style="left:152px;top:322px;width:150px;height:150px;background:#f5d915;transform:rotate(14deg)" role="img" aria-label="Syringe app icon for procedures"></div>
<div class="app-tile" style="left:280px;top:374px;width:180px;height:180px;background:linear-gradient(#5cbf2a,#2a7a12);transform:rotate(-10deg)" role="img" aria-label="Green leaves app icon for natural care"></div>
<div class="app-tile" style="left:766px;top:210px;width:138px;height:130px;background:#ea4a1e;transform:rotate(10deg)" role="img" aria-label="Syringe app icon"></div>
<div class="app-tile" style="left:712px;top:360px;width:172px;height:210px;background:linear-gradient(#fff27a,#f0c61e);transform:rotate(-12deg)" role="img" aria-label="Pill capsule app icon for medication"></div>
<div class="app-tile" style="left:872px;top:400px;width:156px;height:156px;background:#f28a30;transform:rotate(12deg)" role="img" aria-label="Microscope app icon for lab tests"></div>
<div class="app-tile" style="left:1026px;top:352px;width:88px;height:88px;background:#7ab82a;transform:rotate(6deg)" role="img" aria-label="Leaf app icon"></div>

</body>
</html>
```